Business Card Design Project : Tidewell Press

In preparation for market launch, Whistler's Tidewell Press require the development of a business card. Tidewell Press is a Community online publishing web portal. We provide the the city of Whistler located in B.C. (Canada) business directories, News, Classified ads, News, Events and blogs etc.

The main focus of the brand is to help local businesses to corporate with their online advertisement and marketing. Meeting our clients face to face is a must (B2B).

Target Market(s)

The target market is B2B customers. Business Owners to Marketing, advertising Managers

Industry/Entity Type

Business

Requirements
Must have
• - The business card will be two sided.
the BACK side will have our logo which consist of (icon, url,slogan) submited. The logo will be middle and centred.

The FRONT side should have company details:

Company Legal Name: FERNDALE TIDEWELL PRESS

Owen Marsk
Director of Sales & Marketing

www.ferndaletidewell.biz
owen@ferndaletidewell.biz

Phone: 555 014 3826
#2817 - 562 E. Harlow Ave.
Vancouver, B.C. K7P2R4 Canada
Nice to have
• - For the "FRONT" side of our business card. You can separate or re-arrange with our logo components (icon, logo,slogan). It does not have to be together.

Also our company legal name is rather long so arrange or organize the name in a way to make it shorter. Your experience and creativity will have to come in play.
Should not have
• should not have other colors beside logo color and black text (2 colors). Also nothing Three dimensional

```html
<!DOCTYPE html>
<html lang="en">
<head>
<meta charset="utf-8">
<title>Tidewell Press — Business Card</title>
<link rel="stylesheet" href="https://fonts.googleapis.com/css2?family=Quattrocento:wght@400;700&display=swap">
<style>
  :root {
    --brand-blue: #3158f5;
    --mist-grey: #c4ccc0;
    --ink: #0b0b14;
    --paper-light: #dcdcd0;
    --backdrop: #f7f5cf;
  }
  * { box-sizing: border-box; margin: 0; padding: 0; }
  html, body {
    width: 1200px;
    height: 1200px;
    overflow: hidden;
    background: var(--backdrop);
    font-family: "Quattrocento", Georgia, serif;
    color: var(--ink);
  }
  .canvas {
    position: relative;
    width: 1200px;
    height: 1200px;
  }
  .card {
    position: absolute;
    width: 760px;
    height: 430px;
    overflow: hidden;
  }

  /* Back side: brand sign-off */
  .card-back {
    left: 150px;
    top: 95px;
    background: var(--brand-blue);
  }
  .brand-lockup {
    position: absolute;
    left: 0;
    right: 0;
    top: 135px;
    text-align: center;
  }
  .brand-name {
    display: inline-flex;
    align-items: center;
    gap: 18px;
    font-size: 64px;
    font-weight: 700;
    color: var(--ink);
    line-height: 1;
  }
  .brand-dot {
    width: 34px;
    height: 34px;
    border-radius: 50%;
    background: var(--ink);
  }
  .slogan {
    margin-top: 22px;
    font-size: 30px;
    color: var(--ink);
  }
  .back-url {
    position: absolute;
    right: 28px;
    bottom: 26px;
    font-size: 24px;
    color: var(--ink);
  }

  /* Front side: contact details */
  .card-front {
    left: 290px;
    top: 675px;
    background: var(--mist-grey);
  }
  .wave {
    position: absolute;
    inset: 0;
    width: 100%;
    height: 100%;
  }
  .person {
    position: absolute;
    left: 26px;
    top: 38px;
  }
  .person-name {
    font-size: 30px;
    font-weight: 700;
    padding-left: 40px;
  }
  .person-role {
    font-size: 22px;
    margin-top: 4px;
  }
  .person-email {
    font-size: 16px;
    margin-top: 2px;
    padding-left: 24px;
  }
  .corner-mark {
    position: absolute;
    font-weight: 700;
    font-size: 22px;
    line-height: 1;
  }
  .corner-mark-top {
    right: 26px;
    top: 26px;
    color: var(--brand-blue);
  }
  .corner-mark-bottom {
    left: 26px;
    bottom: 24px;
    color: var(--paper-light);
  }
  .company {
    position: absolute;
    right: 28px;
    top: 190px;
    text-align: right;
    line-height: 1;
  }
  .company-name {
    font-size: 36px;
    letter-spacing: 1px;
  }
  .company-sub {
    font-size: 24px;
    letter-spacing: 1px;
    margin-top: 2px;
  }
  .contact {
    position: absolute;
    right: 28px;
    top: 290px;
    text-align: right;
    font-size: 17px;
    line-height: 1.2;
  }
  .contact .country {
    padding-right: 48px;
  }
</style>
</head>
<body>
<main class="canvas">

  <section class="card card-back" aria-label="Card back">
    <div class="brand-lockup">
      <div class="brand-name"><span class="brand-dot"></span>Tidewell Press</div>
      <p class="slogan">Your Information Gateway</p>
    </div>
    <p class="back-url">www.ferndaletidewell.biz</p>
  </section>

  <section class="card card-front" aria-label="Card front">
    <svg class="wave" viewBox="0 0 760 430" preserveAspectRatio="none" aria-hidden="true">
      <path d="M0 255 C 120 330, 260 320, 380 250 C 500 180, 600 100, 700 105 C 730 107, 750 120, 760 135 L 760 430 L 0 430 Z" fill="var(--brand-blue)"/>
    </svg>

    <div class="corner-mark corner-mark-top">Tidewell Press</div>

    <div class="person">
      <p class="person-name">Owen Marsk</p>
      <p class="person-role">Director of Sales &amp; Marketing</p>
      <p class="person-email">owen@ferndaletidewell.biz</p>
    </div>

    <div class="company">
      <p class="company-name">FERNDALE TIDEWELL</p>
      <p class="company-sub">PRESS</p>
    </div>

    <address class="contact" style="font-style: normal;">
      <p>Phone: 555 014 3826</p>
      <p>#2817 - 562 E. Harlow Ave.</p>
      <p>Vancouver, B.C. K7P2R4</p>
      <p class="country">CANADA</p>
    </address>

    <div class="corner-mark corner-mark-bottom">Tidewell Press</div>
  </section>

</main>
</body>
</html>
```